Inspirational speaker and coach Corinne Valbeck is building a website

Design, Create and launch a 10-15 page Wordpress website. Please research Corinne online and use examples you have access to.

```html
<!DOCTYPE html>
<html lang="en">
<head>
<meta charset="utf-8">
<title>Corinne Valbeck – Inspirational Speaker and Coach</title>
<link rel="stylesheet" href="https://fonts.googleapis.com/css2?family=Prata&family=Roboto:ital,wght@0,400;0,500;0,700;1,400&display=swap">
<style>
:root{
  --blue:#1e4585;
  --blue-dark:#153a7a;
  --orange:#f26b2b;
  --charcoal:#404040;
  --ink:#222;
  --body:#333;
  --grey-btn:#5a5a5a;
  --white:#fff;
}
*{box-sizing:border-box;margin:0;padding:0}
html,body{width:1200px;height:5208px;overflow:hidden;background:#fff}
body{position:relative;font-family:"Roboto",Arial,sans-serif;color:var(--body)}
section,header,footer{position:absolute;left:0;width:1200px;overflow:hidden}
.abs{position:absolute}
.serif{font-family:"Prata",Georgia,serif;font-weight:400;text-transform:uppercase}
.btn{position:absolute;display:flex;align-items:center;justify-content:center;background:var(--orange);color:#fff;font:700 15px "Roboto",Arial,sans-serif;text-transform:uppercase;letter-spacing:.3px;white-space:nowrap}
.btn.grey{background:var(--grey-btn)}
.para{font-size:13.5px;line-height:30px}
.photo{position:absolute}

/* hero */
.hero{top:0;height:687px;background:linear-gradient(180deg,#6f8fb2 0%,#8aa0a8 30%,#5e6f52 60%,#3e5c3a 100%)}
.hero .city{left:0;top:0;width:1200px;height:600px;background:linear-gradient(90deg,rgba(40,60,50,.35),rgba(90,100,90,.1) 50%,rgba(60,60,40,.2))}
.hero .portrait{left:660px;top:40px;width:500px;height:560px;background:radial-gradient(ellipse at 50% 40%,#e8dcc0 0%,#b99c6a 35%,#6a5a3a 70%,rgba(60,60,40,0) 100%)}
.nav{top:22px;left:100px;width:1000px;height:40px;display:flex;align-items:center}
.brand{font-size:28px;color:#fff;letter-spacing:.3px;white-space:nowrap}
.menu{margin-left:auto;display:flex;list-style:none}
.menu li{font-size:14px;color:#fff;text-transform:uppercase;margin-left:46px;white-space:nowrap}
.hero h1{left:60px;width:620px;text-align:center;color:#fff;white-space:nowrap}
.hero .hi{top:186px;font:500 42px "Roboto",sans-serif}
.hero .name{top:240px;font-size:46px;line-height:60px;letter-spacing:-.5px}
.hero .role{top:313px;font:500 27px "Roboto",sans-serif;text-transform:uppercase}
.newsletter h2{left:141px;top:560px;color:#fff;font-size:28px;white-space:nowrap}
.field{position:absolute;top:608px;height:47px;background:#fff;font-size:14px;color:#444;display:flex;align-items:center;padding-left:20px;gap:6px}

/* about */
.about{top:687px;height:623px;background:#fff}
.about h2{right:857px;top:118px;text-align:right;font-size:28px;line-height:34px;color:var(--ink);white-space:nowrap}
.about .tag{right:857px;top:196px;color:var(--orange);font:700 12.5px Roboto,sans-serif;text-transform:uppercase;white-space:nowrap}
.about .sign{left:190px;top:218px;width:160px;height:54px;background:linear-gradient(90deg,#f4f4f4,#e9e9e9)}
.about .rule{left:262px;top:280px;width:88px;height:3px;background:var(--orange)}
.about .text{left:386px;top:104px;width:290px;color:#444;font-size:13px;line-height:24px}
.about .circle{left:698px;top:93px;width:402px;height:402px;border-radius:50%;background:radial-gradient(circle at 50% 40%,#e8e2d6,#a9a7a2 50%,#2e2e2e 90%)}

/* services */
.services{top:1310px;height:690px;background:var(--blue)}
.services .ring{left:0;top:-10px}
.services .person{left:172px;top:74px;width:343px;height:616px;background:linear-gradient(180deg,#efe8d8 0%,#a38b52 35%,#6b5a30 70%,#2e2e2e 100%);border-radius:150px 150px 0 0}
.services h2{left:667px;top:106px;color:#fff;font-size:32px;white-space:nowrap}
.services .text{left:668px;top:158px;width:440px;color:#fff}

/* why */
.why{top:2000px;height:602px;background:linear-gradient(90deg,#f4f4f4,#e6e6e6)}
.why .photo{left:560px;top:0;width:640px;height:602px;background:linear-gradient(120deg,#c9d3dc 0%,#efe9dc 35%,#a89a84 65%,#3d3a38 100%);clip-path:polygon(20% 0,100% 0,100% 100%,0 100%)}
.why h2{left:152px;top:98px;font-size:32px;color:var(--ink);white-space:nowrap}
.why .text{left:155px;top:150px;width:440px;color:#333}

/* testimonials */
.testimonials{top:2602px;height:768px;background:var(--charcoal)}
.testimonials h2{left:0;width:1200px;text-align:center;top:74px;font-size:32px;color:#fff}
.testimonials .sub{left:0;width:1200px;text-align:center;top:122px;font-size:13px;color:#fff}
.card{position:absolute;background:#555;overflow:hidden}
.card .shot{position:absolute;left:0;top:0;width:100%}
.card .who{position:absolute;width:100%;text-align:center;color:var(--orange);font-size:19px}
.card .quote{position:absolute;width:100%;text-align:center;color:#fff;font-style:italic;font-size:13.5px;line-height:22px;padding:0 40px}
.arrow{position:absolute;width:46px;height:46px;border-radius:50%;background:#fff;display:flex;align-items:center;justify-content:center}
.dots{left:0;width:1200px;top:675px;display:flex;justify-content:center;gap:16px}
.dots i{width:10px;height:10px;border-radius:50%;background:#777}
.dots i.on{background:#ddd}

/* blog */
.blog{top:3370px;height:707px;background:#fff}
.blog h2{left:0;width:1200px;text-align:center;top:88px;font-size:32px;color:var(--ink)}
.blog .sub{left:0;width:1200px;text-align:center;top:136px;font-size:13.5px;color:#222}
.post{position:absolute;left:150px;width:360px}
.post .meta{font-size:11.5px;color:#444}
.post h3{font:700 17px/21px Roboto,sans-serif;color:#222;margin-top:8px}
.post .more{margin-top:16px;font:700 11px Roboto,sans-serif;color:#222;text-transform:uppercase;display:inline-flex;align-items:center;gap:8px;border-bottom:2px solid var(--orange);padding-bottom:4px}
.feature{left:560px;top:216px;width:503px;height:410px;background:linear-gradient(180deg,#9b8f80 0%,#6f6b6c 45%,#3f4656 100%)}
.feature .meta{position:absolute;left:21px;top:306px;color:#fff;font-size:12px}
.feature .title{position:absolute;left:21px;top:332px;width:440px;color:#fff;font:500 17px/31px Roboto,sans-serif}
.navsq{position:absolute;top:178px;width:36px;height:50px;background:var(--orange);display:flex;align-items:center;justify-content:center}

/* book */
.book{top:4077px;height:533px;background:linear-gradient(90deg,#5f5f5f,#767676 55%,#8d8d8d)}
.book .photo{left:606px;top:0;width:594px;height:533px;background:radial-gradient(ellipse at 55% 40%,#e6e6e6 0%,#a9a9a9 40%,#3a3a3a 85%)}
.book h2{left:124px;top:104px;font-size:32px;color:#fff;white-space:nowrap}
.book .text{left:128px;top:154px;width:440px;color:#fff}

/* featured */
.featured{top:4610px;height:303px;background:#fff}
.featured h2{left:0;width:1200px;text-align:center;top:80px;font-size:26px;color:var(--ink);white-space:nowrap}
.logos{left:140px;width:920px;top:150px;height:60px;display:flex;justify-content:space-between;align-items:center}
.logos span{font:400 30px "Prata",Georgia,serif;color:#666;display:flex;align-items:center;gap:10px;white-space:nowrap}
.logos .box{width:44px;height:44px;border:3px solid #666}

/* footer */
.footer{top:4913px;height:295px;background:var(--blue-dark)}
.footer .name{left:0;width:1200px;text-align:center;top:60px;font-size:24px;color:#fff}
.footer .links{left:0;width:1200px;top:124px;display:flex;justify-content:center;gap:50px;list-style:none}
.footer .links li{font:500 14.5px Roboto,sans-serif;color:#fff;text-transform:uppercase}
.footer .social{left:0;width:1200px;top:180px;display:flex;justify-content:center;gap:12px}
.footer .social i{width:34px;height:34px;border-radius:50%;border:1.5px solid #fff}
.footer .copy{left:0;width:1200px;text-align:center;top:240px;color:#fff;font-size:12.5px}
</style>
</head>
<body>

<header class="hero">
  <div class="photo city" role="img" aria-label="City skyline with mountains behind"></div>
  <div class="photo portrait" role="img" aria-label="Portrait of Corinne Valbeck holding out a tiara"></div>
  <div class="abs nav">
    <div class="brand serif">Corinne Valbeck</div>
    <ul class="menu"><li>Home</li><li>About</li><li>Blogs</li><li>Podcasts</li><li>Speaking</li><li>Contact</li></ul>
  </div>
  <h1 class="abs hi">HI, I AM</h1>
  <h1 class="abs name serif">Corinne Valbeck</h1>
  <h1 class="abs role">Inspirational Speaker and Coach</h1>
  <div class="btn" style="left:297px;top:370px;width:143px;height:44px">Learn More</div>
  <svg class="abs" style="left:0;top:480px" width="1200" height="207" viewBox="0 0 1200 207">
    <path d="M0 22 C300 55 600 60 900 20 C1000 8 1100 30 1200 34 L1200 207 L0 207 Z" fill="#1e4585"/>
  </svg>
  <div class="newsletter">
    <h2 class="abs serif">Sign up for newsletter</h2>
    <div class="field" style="left:139px;width:376px">
      <svg width="11" height="12" viewBox="0 0 11 12"><circle cx="5.5" cy="3.2" r="3" fill="#444"/><path d="M0 12c0-4 2.5-5.5 5.5-5.5S11 8 11 12z" fill="#444"/></svg>First Name</div>
    <div class="field" style="left:527px;width:376px">
      <svg width="13" height="10" viewBox="0 0 13 10"><rect width="13" height="10" fill="#444"/><path d="M0 0l6.5 5L13 0" stroke="#fff" fill="none"/></svg>Email</div>
    <div class="btn" style="left:915px;top:608px;width:143px;height:47px">Submit</div>
  </div>
</header>

<section class="about">
  <h2 class="abs serif">About Corinne<br>Valbeck</h2>
  <div class="abs tag">Inspirational Speaker and Coach</div>
  <div class="abs sign" role="img" aria-label="Handwritten signature of Corinne Valbeck"></div>
  <div class="abs rule"></div>
  <div class="abs text">
    <p>Lorem ipsum dolor sit amet, constur adipiscing elit, sed do eiusmod tempor incididunt ut labore et dolore magna aliqua. Quissum suspendisse ultrices gravida. Risus comdo viverra maecenas accumsan lacus vel facilisis. Lorem ipsum dolor sit amet, constur aelit, sed do eiusmod tempor incididunt ut labore ore magna aliqua. Quissum suspendisseLorem ip dolor sit amet, constur adipiscing elit, sed do eiusmod</p>
    <p style="margin-top:18px">Lorem ipsum dolor sit amet, constur adipiscing elit, sed do eiusmod tempor incididunt ut labore et dolore magna aliqua.</p>
  </div>
  <div class="btn" style="left:386px;top:440px;width:155px;height:43px">Learn More</div>
  <div class="abs circle" role="img" aria-label="Close-up portrait of Corinne Valbeck with braided blonde hair"></div>
</section>

<section class="services">
  <svg class="abs ring" width="540" height="520" viewBox="0 0 540 520"><circle cx="263" cy="245" r="250" fill="none" stroke="#7d93b8" stroke-width="12" opacity=".8"/></svg>
  <div class="photo person" role="img" aria-label="Corinne Valbeck standing in a patterned blouse"></div>
  <h2 class="abs serif">What do I do</h2>
  <div class="abs text para">
    <p>Lorem ipsum dolor sit amet, consectetur adiiscing elit, sed do eiusmod tempor incididunt ore et dolore magna aliqua. Quis ipsum suspendisse ultrices gravida. Risus commodo viverra maecenas accumsan lacus vel facilisis. Lorem ipsum dolor sit amet, consectcing elit, sed do eiusmod tempor incididunt ore et dolore magna aliqua.</p>
    <p style="margin-top:14px">Lorem ipsum dolor sit amet, consectetur adiiscing elit, sed do eiusmod tempor incididunt ore et dolore magna aliqua. Quis ipsum suspendisse ultrices gravida. Risus commodo viverra maecenas accumsan lacus vel facilisis. Lorem ipsum dolor sit amet, consectcing elit, sed do eiusmod tempor incididunt ore et dolore magna aliquarem ipsum dolor sit amet, consectetur adiiscing elit, sed do eiusmod te</p>
  </div>
  <div class="btn" style="left:665px;top:530px;width:280px;height:45px">More about my services</div>
</section>

<section class="why">
  <div class="photo" role="img" aria-label="Smiling Corinne Valbeck holding a black notebook"></div>
  <h2 class="abs serif">Why M I helping you</h2>
  <div class="abs text para">
    <p>Lorem ipsum dolor sit amet, consectetur adiiscing elit, sed do eiusmod tempor incididunt ore et dolore magna aliqua. Quis ipsum suspendisse ultrices gravida. Risus commodo viverra maecenas accumsan lacus vel facilisis. Lorem ipsum dolor sit amet, consectcing elit, sed do eiusmod tempor incididunt ore et dolore magna aliqua.</p>
    <p style="margin-top:6px">Lorem ipsum dolor sit amet, consectetur adiiscing elit, sed do eiusmod tempor incididunt ore et dolore magna aliqua. Quis ipsum suspendisse ultrices gravida. Risus commodo viverra maecenas accumsan lacus vel facilisis. Lorem ipsum dolor sit amet,</p>
  </div>
  <div class="btn" style="left:158px;top:462px;width:153px;height:43px">Learn More</div>
  <div class="btn grey" style="left:321px;top:462px;width:156px;height:43px">Contact Me</div>
</section>

<section class="testimonials">
  <h2 class="abs serif">Customer testimonials</h2>
  <div class="abs sub">Look Below to See Why We're Proud</div>

  <div class="card" style="left:-10px;top:206px;width:260px;height:390px">
    <div class="shot" style="height:294px;background:linear-gradient(180deg,#3a2a24,#7a5a4a 50%,#2a2020)" role="img" aria-label="Video still of a client testimonial"></div>
    <div class="quote" style="top:318px;text-align:left;padding:0 0 0 10px">ipiscing elit, sed do eiusmod tempor ore magna aliqua.</div>
  </div>
  <div class="card" style="left:970px;top:206px;width:240px;height:390px">
    <div class="shot" style="height:294px;background:linear-gradient(180deg,#5a5a4a,#8a7868 55%,#3a3632)" role="img" aria-label="Video still of a client testimonial"></div>
    <div class="quote" style="top:318px;text-align:left;padding:0 0 0 46px">Lorem ipsum dolor sit amet, con incididunt ut l</div>
  </div>
  <div class="arrow" style="left:100px;top:364px"><svg width="22" height="16" viewBox="0 0 22 16"><path d="M21 8H2M8 1L1 8l7 7" stroke="#f26b2b" stroke-width="2" fill="none"/></svg></div>
  <div class="arrow" style="left:1014px;top:364px"><svg width="22" height="16" viewBox="0 0 22 16"><path d="M1 8h19M14 1l7 7-7 7" stroke="#888" stroke-width="2" fill="none"/></svg></div>

  <div class="card" style="left:297px;top:180px;width:626px;height:444px">
    <div class="shot" style="height:330px;background:linear-gradient(180deg,#b8c9da 0%,#c98a5a 45%,#a5603a 75%,#7a5a3e 100%)" role="img" aria-label="Client with arms raised above a red rock canyon"></div>
    <svg class="abs" style="left:275px;top:127px" width="76" height="76" viewBox="0 0 76 76"><circle cx="38" cy="38" r="35" fill="rgba(0,0,0,.25)" stroke="#fff" stroke-width="4"/><path d="M30 24l22 14-22 14z" fill="#fff"/></svg>
    <div class="who" style="top:354px">Daniel Ortiz</div>
    <div class="quote" style="top:382px">Lorem ipsum dolor sit amet, consectetur adipiscing elit, sed do eiusmod tempor incididunt ut labore et dolore magna aliqua.</div>
  </div>
  <div class="abs dots"><i></i><i></i><i class="on"></i><i></i><i></i></div>
</section>

<section class="blog">
  <h2 class="abs serif">From the blog</h2>
  <div class="abs sub">Each one of my blog posts is infused with passion and laced with optimism</div>

  <article class="post" style="top:234px">
    <div class="meta">by Corinne Valbeck | Aug 13 2021</div>
    <h3>Finibus Bonorum et Malorum", written by Lucius Brenn in 45 BC</h3>
    <div class="more">Read More <svg width="18" height="10" viewBox="0 0 18 10"><path d="M0 5h16M12 1l4 4-4 4" stroke="#222" fill="none" stroke-width="1.5"/></svg></div>
  </article>
  <article class="post" style="top:374px">
    <div class="meta">by Corinne Valbeck | Aug 13 2021</div>
    <h3>Finibus Bonorum et Malorum", written by Lucius Brenn in 45 BC</h3>
    <div class="more">Read More <svg width="18" height="10" viewBox="0 0 18 10"><path d="M0 5h16M12 1l4 4-4 4" stroke="#222" fill="none" stroke-width="1.5"/></svg></div>
  </article>
  <article class="post" style="top:518px">
    <div class="meta">by Corinne Valbeck | Aug 13 2021</div>
    <h3>Finibus Bonorum et Malorum", written by Lucius Brenn in 45 BC</h3>
    <div class="more">Read More <svg width="18" height="10" viewBox="0 0 18 10"><path d="M0 5h16M12 1l4 4-4 4" stroke="#222" fill="none" stroke-width="1.5"/></svg></div>
  </article>

  <div class="abs feature" role="img" aria-label="Group photo of a family gathering with balloons">
    <div class="navsq" style="left:0"><svg width="12" height="20" viewBox="0 0 12 20"><path d="M10 2L2 10l8 8" stroke="#fff" stroke-width="2.5" fill="none"/></svg></div>
    <div class="navsq" style="right:0"><svg width="12" height="20" viewBox="0 0 12 20"><path d="M2 2l8 8-8 8" stroke="#fff" stroke-width="2.5" fill="none"/></svg></div>
    <div class="meta">by Corinne Valbeck | Aug 13 2021</div>
    <div class="title">Lorem ipsum dolor sit amet, consecur adipiscing elit, sed do eiusmod tempor incididunt</div>
  </div>
</section>

<section class="book">
  <div class="photo" role="img" aria-label="Black and white portrait of Corinne Valbeck smiling"></div>
  <h2 class="abs serif">Book me to speak</h2>
  <div class="abs text para">
    <p>Lorem ipsum dolor sit amet, consectetur adiiscing elit, sed do eiusmod tempor incididunt ore et dolore magna aliqua. Quis ipsum suspendisse ultrices gravida.</p>
    <p style="margin-top:8px">Lorem ipsum dolor sit amet, consectetur adiiscing elit, sed do eiusmod tempor incididunt ore et dolore magna aliqua. Quis ipsum suspendisse ultrices gravida. Risus commodo viverra maecenas accumsan lacus vel facilisis. Lorem ipsum dolor sit amet, c</p>
  </div>
  <div class="btn" style="left:125px;top:391px;width:239px;height:43px">Book me to speak</div>
</section>

<section class="featured">
  <h2 class="abs serif"># 1 Best-selling author and has been featured in</h2>
  <div class="abs logos">
    <span>Ledgerline</span>
    <span>shopvale.com</span>
    <span>Venture.</span>
    <span><i class="box"></i>Daily Meridian</span>
  </div>
</section>

<footer class="footer">
  <div class="abs name serif">Corinne Valbeck</div>
  <ul class="abs links"><li>Home</li><li>About</li><li>Blogs</li><li>Podcasts</li><li>Speaking</li><li>Contact</li></ul>
  <div class="abs social" aria-label="Social profiles"><i></i><i></i><i></i><i></i></div>
  <div class="abs copy">©Copyright ©2021 Corinne Valbeck . All Rights Reserved.</div>
</footer>

</body>
</html>
```